Recruitment Site Design

We need a design for the login page, about page, and inner pages of a recruitment site for an oil and gas company. Design should be modern, sleek, professional and colors can be blue, green, white, orange or any other recommended colors.

Please also take into consideration that once the users login, they will need to access a form to fill in their information.

** UPDATE: Kindly provide a design for the inner information page consistent with the outer design. Attached is a picture of the basic structure. ***
Updates

Please provide a design for inner pages as shown in the design brief consistent with the registration page provided. 

Reason: We're extending it to get more inside pages.

Target Market(s)

Professionals looking for a career in the oil and gas industry in the Middle East.

Industry/Entity Type

Oil And Gas

Requirements
Must have
• Sleek design

```html
<!DOCTYPE html>
<html lang="en">
<head>
<meta charset="utf-8">
<title>Login</title>
<link rel="stylesheet" href="https://fonts.googleapis.com/css2?family=Arimo:wght@400;700&family=Open+Sans:ital,wght@0,400;0,600;1,400&family=PT+Sans+Narrow&display=swap">
<style>
  :root {
    --header-bg: #222220;
    --logo-grey: #d2d2d2;
    --green: #5aa539;
    --green-light: #8fcc6a;
    --green-dark: #4c9a2c;
    --page-bg: #ebe9e9;
    --box-border: #bdbdbd;
    --field-border: #d6d6d6;
    --placeholder: #a8a8a8;
    --label: #333333;
    --muted: #6f6f6f;
    --link-blue: #1ea0e6;
    --footer-rule: #5a5a5a;
    --footer-bg: #a0a0a2;
    --white: #ffffff;
  }
  * { box-sizing: border-box; margin: 0; padding: 0; }
  html, body { width: 1200px; height: 762px; overflow: hidden; }
  body { position: relative; background: var(--page-bg); font-family: "Arimo", Arial, sans-serif; }

  .site-header { position: absolute; left: 0; top: 0; width: 1200px; height: 67px; background: var(--header-bg); }
  .brand { position: absolute; left: 188px; top: 10px; font: 700 38px/46px "Arimo", Arial, sans-serif; color: var(--logo-grey); }
  .account-links { position: absolute; left: 830px; top: 18px; font: 400 12px/16px "Open Sans", sans-serif; color: var(--white); word-spacing: 2px; }

  .main-nav { position: absolute; left: 0; top: 67px; width: 1200px; height: 39px;
    background: linear-gradient(#9fd47d 0, #6cb546 30%, var(--green-dark) 100%); border-top: 2px solid #cfe9bd; }
  .main-nav .home { position: absolute; left: 203px; top: 9px; }
  .main-nav a { position: absolute; top: 11px; font: 700 13px/16px "Arimo", Arial, sans-serif; color: var(--white); text-decoration: none; }
  .main-nav a.current { color: #1a1a1a; }

  .site-title { position: absolute; left: 0; width: 1016px; top: 155px; text-align: center; font: 400 46px/52px "Arimo", Arial, sans-serif; color: var(--green); }

  .login-box { position: absolute; left: 314px; top: 214px; width: 393px; height: 308px;
    background: linear-gradient(#ffffff, #f4f4f4); border: 1px solid var(--box-border); border-radius: 10px; }
  .login-box h1 { position: absolute; left: 25px; top: 17px; font: 700 30px/38px "Open Sans", sans-serif; color: #111; }
  .field-label { position: absolute; left: 22px; font: 600 13px/16px "Open Sans", sans-serif; color: var(--label); }
  .field { position: absolute; left: 22px; width: 356px; height: 43px; background: var(--white);
    border: 1px solid var(--field-border); border-radius: 5px; font: 400 13px/41px "Arimo", Arial, sans-serif; color: var(--placeholder); }
  .check { position: absolute; left: 22px; width: 19px; height: 19px; background: var(--white); border: 1px solid var(--field-border); border-radius: 3px; }
  .check-label { position: absolute; left: 48px; font: 400 12px/19px "Open Sans", sans-serif; color: #111; letter-spacing: -0.3px; }
  .login-button { position: absolute; left: 248px; top: 248px; width: 128px; height: 44px; border-radius: 4px;
    background: linear-gradient(#92cc70, var(--green-dark)); color: var(--white); font: 600 17px/44px "Open Sans", sans-serif; text-align: center; }

  .register-note { position: absolute; left: 0; width: 1006px; top: 532px; text-align: center; font: 400 13px/16px "Arimo", Arial, sans-serif; color: var(--muted); }
  .register-note a { color: var(--link-blue); text-decoration: none; }

  .footer-rule { position: absolute; left: 0; top: 581px; width: 1200px; height: 6px; background: var(--footer-rule); }
  .site-footer { position: absolute; left: 0; top: 587px; width: 1200px; height: 147px; background: var(--footer-bg); color: var(--white); }
  .footer-col { position: absolute; top: 10px; }
  .footer-col h2 { font: 400 18px/24px "PT Sans Narrow", sans-serif; margin-bottom: 6px; }
  .footer-col li { list-style: none; font: 400 11px/20px "Open Sans", sans-serif; padding-left: 3px; }
  .news-item { position: relative; width: 235px; font: 400 11px/15px "Open Sans", sans-serif; padding-left: 4px; margin-bottom: 15px; }
  .news-item em { display: block; font-style: italic; }
  .news-date { position: absolute; right: 0; top: 0; }

  .copyright { position: absolute; left: 0; top: 734px; width: 1200px; height: 28px; background: var(--green);
    color: var(--white); font: 600 10px/28px "Open Sans", sans-serif; text-align: center; }
</style>
</head>
<body>
  <header class="site-header">
    <div class="brand">Company Logo</div>
    <div class="account-links">My Account&nbsp; Registered</div>
  </header>

  <nav class="main-nav">
    <svg class="home" width="20" height="18" viewBox="0 0 20 18" aria-label="Home">
      <path d="M10 1 L1 9.5 H4 V17 H8.5 V12 H11.5 V17 H16 V9.5 H19 Z" fill="#ffffff"/>
    </svg>
    <a style="left:238px">Categories</a>
    <a style="left:332px">Get Stared</a>
    <a style="left:426px">Brows Projects</a>
    <a style="left:547px">Portfolios</a>
    <a class="current" style="left:632px">About Us</a>
  </nav>

  <div class="site-title">COMPANY LOG</div>

  <section class="login-box">
    <h1>Login</h1>
    <div class="field-label" style="top:76px">Username</div>
    <div class="field" style="top:96px; padding-left:29px">Enter your Username or e-mail</div>
    <div class="field-label" style="top:153px">Password</div>
    <div class="field" style="top:173px; padding-left:37px">Enter Password . . .</div>
    <div class="check" style="top:246px"></div>
    <div class="check-label" style="top:246px">I forgot my password</div>
    <div class="check" style="top:271px"></div>
    <div class="check-label" style="top:271px">Stay logged-in</div>
    <div class="login-button">Login</div>
  </section>

  <p class="register-note">You don't have account? Please <a>Registered</a></p>

  <div class="footer-rule"></div>
  <footer class="site-footer">
    <div class="footer-col" style="left:205px">
      <h2>Support</h2>
      <ul><li>Client Integration</li><li>Improved Performance</li><li>Customer Support</li><li>Our Business Helpline</li></ul>
    </div>
    <div class="footer-col" style="left:362px">
      <h2>Financial Success</h2>
      <ul><li>Consequat Nunc Nibh</li><li>Improved Performance</li><li>Proin Cras Vault</li><li>Our Business Helpline</li><li>Voluptous</li></ul>
    </div>
    <div class="footer-col" style="left:543px">
      <h2>Business Guidelines</h2>
      <ul style="padding-left:9px; padding-top:5px"><li>Client Integration</li><li>Improved Performance</li><li>Customer Support</li><li>Our Business Helpline</li></ul>
    </div>
    <div class="footer-col" style="left:745px">
      <h2>Latest News &amp; Events</h2>
      <div style="padding-top:14px">
        <div class="news-item">Cras Quam Nibh Fullem Nest<span class="news-date">4/21/11</span><em>Loresto mesernt maruis neterin</em></div>
        <div class="news-item" style="width:220px">Mauris Netrern<span class="news-date">4/11/11</span><em>Mesernt maruis neterin</em></div>
      </div>
    </div>
  </footer>
  <div class="copyright">©2011 All Rights Reserved</div>
</body>
</html>
```